Corporate holiday e-card

We’re looking for a fun, energetic and personable winter holiday e-card design to send to our B2B customers. It should not reference a specific holiday; but it can refer to the ‘joys of the season’ or something similar, and also the ‘New Year.’ The design does not need to incorporate specific copy, but it could if integral to the design. Ideally the e-card would incorporate some aspects of the following:

- Our brand identity: elements from our company logo, such as the triad-plug graphic; images from our website; colors; etc.

-Winter themes such as snow, mountains, skiing, etc. are preferable.

-Tie-into our main market: software company providing resources for the renewable energy industry, primarily solar (for more information on the types of products we provide, see our website: www.brightmesa.example).

-We are open to the use of photographic or graphical images. We prefer a clean, modern, technology-oriented look/feel.

The card will be distributed via email, and as such, should be of appropriate size (both dimensionally and file-size).

Target Market(s)

B2B clean-energy

Industry/Entity Type

Software

Font styles to use
Sans Serif

Requirements
Must have
• -Incorporate elements of our brand identity (such as logo, colors, images, etc.)
-Appropriately formatted (dimensions & file size) for email distribution as an image.
Nice to have
• - Play off the winter theme, and incorporate an element of our main business area: solar energy.

```html
<!DOCTYPE html>
<html lang="en">
<head>
<meta charset="utf-8">
<title>Happy Holidays 2013 – Bright Mesa</title>
<link rel="stylesheet" href="https://fonts.googleapis.com/css2?family=Comfortaa:wght@300;400&display=swap">
<style>
  :root {
    --card-grey: #636467;
    --snow-white: #ffffff;
    --frost-blue: #4fb3e0;
    --soft-white: #e8e8ea;
  }
  html, body {
    margin: 0;
    padding: 0;
    width: 1200px;
    height: 1200px;
    overflow: hidden;
    background: var(--card-grey);
  }
  .holiday-card {
    position: relative;
    width: 1200px;
    height: 1200px;
    overflow: hidden;
    background: var(--card-grey);
    font-family: "Comfortaa", sans-serif;
  }
  .snowflake-wreath {
    position: absolute;
    left: 0;
    top: 0;
    width: 1200px;
    height: 1200px;
  }
  .greeting {
    position: absolute;
    left: 816px;
    top: 384px;
    transform: translateX(-50%);
    text-align: center;
    white-space: nowrap;
  }
  .greeting-title {
    margin: 0;
    font-weight: 300;
    font-size: 53px;
    line-height: 1.2;
    color: var(--frost-blue);
  }
  .greeting-year {
    margin: 22px 0 0;
    font-weight: 300;
    font-size: 38px;
    line-height: 1.2;
    color: var(--soft-white);
  }
  .brand-sign {
    position: absolute;
    left: 42px;
    top: 1040px;
    display: flex;
    align-items: center;
    gap: 12px;
  }
  .brand-dot {
    width: 26px;
    height: 26px;
    border-radius: 50%;
    background: var(--frost-blue);
  }
  .brand-name {
    font-weight: 400;
    font-size: 36px;
    color: var(--frost-blue);
  }
  .thank-you {
    position: absolute;
    left: 38px;
    top: 1130px;
    margin: 0;
    font-weight: 300;
    font-size: 31px;
    line-height: 1.2;
    color: var(--soft-white);
  }
</style>
</head>
<body>
  <main class="holiday-card">
    <svg class="snowflake-wreath" viewBox="0 0 1200 1200" role="img" aria-label="Wreath of white snowflakes with small blue centres forming a large ring">
      <defs>
        <radialGradient id="wreath-glow" cx="816" cy="444" r="530" gradientUnits="userSpaceOnUse">
          <stop offset="0" stop-color="var(--snow-white)" stop-opacity="0"/>
          <stop offset="0.58" stop-color="var(--snow-white)" stop-opacity="0"/>
          <stop offset="0.72" stop-color="var(--snow-white)" stop-opacity="0.45"/>
          <stop offset="0.8" stop-color="var(--frost-blue)" stop-opacity="0.35"/>
          <stop offset="0.88" stop-color="var(--snow-white)" stop-opacity="0.45"/>
          <stop offset="1" stop-color="var(--snow-white)" stop-opacity="0"/>
        </radialGradient>
      </defs>
      <circle cx="816" cy="444" r="530" fill="url(#wreath-glow)"/>
    </svg>

    <div class="greeting">
      <h1 class="greeting-title">Happy Holidays</h1>
      <p class="greeting-year">2013</p>
    </div>

    <div class="brand-sign">
      <span class="brand-dot"></span>
      <span class="brand-name">Bright Mesa</span>
    </div>

    <p class="thank-you">Thank you for your business</p>
  </main>
</body>
</html>
```